Youth Sports Banner Ad - 3x5 ft banner special!

We are looking for a full page ad (8.5x11") to advertise our banner services for Youth Sports leagues. The flyers will be handed out to teams and parents in hopes to draw their business to us for team banners.
We want to show our logo, address (4816 Corliss Ln. Paso Robles). Please include that we are offering a youth sports special price on 3x5 ft team banners for $115 (plus tax). The pricing will include 1 layout with up to 2 revisions. We would like the ad to grab the attention of the audience and ask them to "Call, Email or Stop in Today!"

Our info that needs to be on the banner includes:
email: info@markwell202.example
phone: 805-219-6847

We want to really focus on our quick turnaround as we will be producing the banners withing 1-2 business days after artwork approval.
We would like to include the banner samples if possible, and if you see fit, also include that we would like the potential customer to email us their teams name, roster, and colors to help speed up the layout process.

Target Market(s)

Parents of kids playing youth sports. The flyer is meant to increase awareness of our sign shop, while offering a great discount on banners for youth sports banners.

Font styles to use
Sans Serif

Colors

Designer to choose colors to be used in the design.

Requirements
Must have
• Our logo, $115 plus tax banner price, our business information, request to send over all team information including name, roster, and team colors.
Nice to have
• Would like to see color in the ad! If you can tie in the Kelly green from our logo, that would be great.

```html
<!DOCTYPE html>
<html lang="en">
<head>
<meta charset="utf-8">
<title>Youth Sports Banner Special – Markwell Signs</title>
<link rel="stylesheet" href="https://fonts.googleapis.com/css2?family=Anton&family=Oswald:wght@700&family=Roboto+Condensed:wght@400;700&family=Lato:wght@400&display=swap">
<style>
  :root {
    --page-bg: #e6e6e6;
    --kelly: #36c95f;
    --kelly-bright: #1fef80;
    --kelly-deep: #22b85a;
    --orange: #f7a800;
    --price-yellow: #f6e41c;
    --ink: #111111;
    --white: #ffffff;
    --pin-red: #e8262d;
    --sky-light: #e4eeee;
    --sky-teal: #5c9ea2;
    --grass: #3e7a2e;
    --grass-dark: #17261a;
  }
  * { box-sizing: border-box; margin: 0; padding: 0; }
  html, body {
    width: 1200px; height: 1200px; overflow: hidden;
    background: var(--page-bg);
  }
  .canvas { position: relative; width: 1200px; height: 1200px; overflow: hidden; }

  .flyer {
    position: absolute; left: 165px; top: 40px;
    width: 976px; height: 1256px;
    transform: scale(0.8917); transform-origin: top left;
    overflow: hidden;
    font-family: "Roboto Condensed", sans-serif;
  }

  .backdrop {
    position: absolute; inset: 0;
    background:
      radial-gradient(ellipse 60% 35% at 45% 8%, rgba(255,255,255,.85), rgba(255,255,255,0) 70%),
      linear-gradient(180deg, rgba(0,0,0,0) 0%, rgba(0,0,0,0) 66%, rgba(30,60,30,.55) 72%, var(--grass) 82%, var(--grass-dark) 100%),
      linear-gradient(100deg, var(--sky-light) 0%, #b9d3d3 45%, var(--sky-teal) 100%);
  }

  .player-photo {
    position: absolute; left: 630px; top: 240px; width: 330px; height: 990px;
    border-radius: 160px 160px 40px 40px;
    background: linear-gradient(180deg, rgba(120,200,120,.35) 0%, rgba(54,201,95,.55) 45%, rgba(200,220,200,.35) 80%, rgba(40,60,40,.4) 100%);
  }

  .brand {
    position: absolute; top: 38px; left: 0; width: 976px;
    display: flex; justify-content: center; align-items: center; gap: 20px;
  }
  .brand-mark { width: 110px; height: 110px; background: var(--kelly-deep); }
  .brand-text { display: flex; flex-direction: column; }
  .brand-name {
    font-family: "Oswald", sans-serif; font-weight: 700;
    font-size: 60px; line-height: 1.1; color: var(--ink); letter-spacing: 1px;
  }
  .brand-tagline {
    font-size: 27px; line-height: 1.1; color: var(--ink); letter-spacing: 1px;
  }

  .headline-youth, .headline-sports, .cta-lead, .cta-today {
    position: absolute; white-space: nowrap; transform-origin: left top;
  }
  .headline-youth {
    left: 27px; top: 217px;
    font-family: "Anton", sans-serif; font-size: 183px; line-height: 1;
    color: var(--kelly); transform: scaleX(1.36);
    text-shadow: 2px 4px 4px rgba(0,0,0,.35);
  }
  .headline-sports {
    left: 28px; top: 392px;
    font-weight: 400; font-size: 196px; line-height: 1;
    color: var(--orange); letter-spacing: -8px;
    text-shadow: 3px 4px 4px rgba(0,0,0,.3);
  }

  .offer-panel {
    position: absolute; left: 0; top: 581px; width: 600px; height: 140px;
    clip-path: polygon(0 6%, 98% 0, 100% 100%, 0 94%);
    background: linear-gradient(160deg, var(--kelly-bright), var(--kelly-deep));
    padding: 12px 0 0 27px; color: var(--ink);
  }
  .offer-line { font-size: 33px; line-height: 36px; white-space: nowrap; }
  .offer-line strong { font-weight: 700; }
  .offer-price {
    position: absolute; left: 468px; top: 50px;
    font-family: "Anton", sans-serif; font-size: 56px; line-height: 1;
    color: var(--price-yellow); text-shadow: 2px 3px 3px rgba(0,0,0,.55);
  }
  .offer-note {
    font-family: "Lato", sans-serif; font-size: 15px; line-height: 18px;
    margin-top: 4px; width: 430px;
  }

  .address-bar {
    position: absolute; left: 0; top: 753px; width: 594px; height: 98px;
    clip-path: polygon(0 4%, 98% 0, 100% 100%, 0 92%);
    background: linear-gradient(180deg, #ffffff 0%, #f1f1f1 60%, #cfcfcf 100%);
    display: flex; align-items: center; padding-left: 45px; gap: 18px;
  }
  .address-text { font-weight: 700; font-size: 39px; color: var(--ink); white-space: nowrap; }

  .cta-lead {
    left: 27px; top: 888px;
    font-family: "Anton", sans-serif; font-size: 51px; line-height: 1;
    color: var(--white); transform: scaleX(1.27);
    text-shadow: 2px 3px 3px rgba(0,0,0,.5);
  }
  .cta-today {
    left: 26px; top: 946px;
    font-family: "Anton", sans-serif; font-size: 162px; line-height: 1;
    color: var(--orange); transform: scaleX(1.42);
    text-shadow: 4px 5px 0 #1a1a1a;
  }
  .team-request {
    position: absolute; left: 28px; top: 1104px;
    font-size: 21px; color: var(--white); white-space: nowrap;
  }

  .contact { position: absolute; left: 28px; display: flex; align-items: center; gap: 16px; color: var(--white); }
  .contact-phone { top: 1132px; }
  .contact-email { top: 1182px; }
  .contact-text { font-size: 42px; line-height: 1.1; white-space: nowrap; }
  .contact-phone .contact-text { font-weight: 700; }
</style>
</head>
<body>
<div class="canvas">
  <article class="flyer">
    <div class="backdrop" role="img" aria-label="Stadium sky with bright lights above a blurred green soccer field"></div>
    <div class="player-photo" role="img" aria-label="Young soccer player in a green kit giving a thumbs up with one foot on a soccer ball"></div>

    <header class="brand">
      <span class="brand-mark"></span>
      <span class="brand-text">
        <span class="brand-name">MARKWELL SIGNS</span>
        <span class="brand-tagline">BANNERS IN 1-2 BUSINESS DAYS</span>
      </span>
    </header>

    <h1 class="headline-youth">YOUTH</h1>
    <h2 class="headline-sports">SPORTS</h2>

    <section class="offer-panel">
      <p class="offer-line">We are offering a youth sports special</p>
      <p class="offer-line">price on <strong>3x5 ft</strong> team banners for</p>
      <p class="offer-note">*Plus tax. Includes 1 layout with up to 2 revisions. Ready 1-2 business days after artwork approval.</p>
      <span class="offer-price">$115</span>
    </section>

    <section class="address-bar">
      <svg width="24" height="34" viewBox="0 0 24 34" aria-hidden="true">
        <path d="M12 0C5.4 0 0 5.2 0 11.7 0 20 12 34 12 34s12-14 12-22.3C24 5.2 18.6 0 12 0z" fill="var(--pin-red)"/>
        <circle cx="12" cy="11.5" r="4.5" fill="#fff"/>
      </svg>
      <span class="address-text">4816 Corliss Ln. Paso Robles</span>
    </section>

    <p class="cta-lead">CALL, EMAIL OR STOP IN</p>
    <p class="cta-today">TODAY!</p>
    <p class="team-request">Email us your team name, roster &amp; colors to speed up the layout!</p>

    <p class="contact contact-phone">
      <svg width="44" height="44" viewBox="0 0 44 44" aria-hidden="true">
        <circle cx="22" cy="22" r="19" fill="none" stroke="var(--kelly)" stroke-width="3"/>
        <path d="M15 12c1.5-1 3-.5 3.5.8l1.6 3.6c.4 1-.1 2-.9 2.5l-1.3.8c.9 2.6 3 4.9 5.6 6.1l.9-1.2c.6-.8 1.6-1.1 2.5-.6l3.4 1.9c1.2.7 1.4 2.3.4 3.6-1.5 1.9-3.8 2.6-6.1 1.7-5.4-2.2-9.5-6.6-11.3-12-.8-2.4 0-5.2 1.7-7.2z" fill="var(--kelly)"/>
      </svg>
      <span class="contact-text">805-219-6847</span>
    </p>
    <p class="contact contact-email">
      <svg width="44" height="30" viewBox="0 0 40 28" aria-hidden="true">
        <rect x="0" y="0" width="40" height="28" fill="var(--kelly)"/>
        <path d="M1 1l19 15L39 1M1 27l14-13M39 27L25 14" fill="none" stroke="#17261a" stroke-width="2"/>
      </svg>
      <span class="contact-text">info@markwell202.example</span>
    </p>
  </article>
</div>
</body>
</html>
```